依頼詳細
毎月ポスティングを3万枚は配布するので、ターゲットをしっかりしぼったチラシ作成をお願いします。

女性30~45歳 ゆっくりと上質な接客サービスをうけたい
髪を傷めないサロン
近郊美容室の2倍の価格で5年目を迎えました。
記載項目
Le Chêne Doré (ルシェヌドレ) 092-478-5126 完全予約制 上質空間 髪質改善 ワンランク上のサービス 髪を傷めない 一生のお付き合いを https://salon.kamisearch-example.jp/slnK000571832/
サイズ
A4
ページ数
両面
希望イメージ
シンプル 複雑
単色 カラフル
暗い 明るい
日常 高級
遊び心 厳粛
未来的 伝統的
女性的 男性的
希望する色
大人女性が目に付く配色
納品ファイル
• 高解像度JPG (.jpg)
補足説明
年間で数回のチラシ制作を依頼してるのですが、なかなかぐっとこなくて・・・。
継続で依頼していきたいのでお願いします

```html
<!DOCTYPE html>
<html lang="ja">
<head>
<meta charset="utf-8">
<title>Le Chêne Doré 完全予約制</title>
<link href="https://fonts.googleapis.com/css2?family=Shippori+Mincho:wght@400;600;700;800&family=Cormorant+Garamond:wght@500;600&family=Noto+Sans+JP:wght@400;500&display=swap" rel="stylesheet">
<style>
  :root {
    --navy: #1d2a4b;
    --navy-deep: #17223f;
    --gold: #c6a15a;
    --gold-dark: #a9843f;
    --gold-light: #e6cf98;
    --cream: #f8f4ea;
    --paper: #fdfcf8;
    --ink: #3a342c;
    --white: #ffffff;
  }
  * { box-sizing: border-box; margin: 0; padding: 0; }
  html, body { width: 849px; height: 1200px; overflow: hidden; background: var(--white); }
  .flyer {
    position: relative; width: 849px; height: 1200px; overflow: hidden;
    background: var(--paper);
    font-family: "Shippori Mincho", serif; color: var(--ink);
  }
  .pattern-top {
    position: absolute; left: 0; top: 0; width: 849px; height: 500px;
    background: radial-gradient(circle at 15% 20%, #2d3b62 0, transparent 28%),
                radial-gradient(circle at 85% 15%, #2d3b62 0, transparent 26%),
                linear-gradient(180deg, var(--navy), #22305a);
  }
  .reserve-banner {
    position: absolute; left: 242px; top: 26px; width: 365px; height: 50px;
    background: linear-gradient(90deg, var(--gold-dark), var(--gold-light) 50%, var(--gold-dark));
    color: var(--white); font-size: 32px; font-weight: 700; letter-spacing: 8px;
    display: flex; align-items: center; justify-content: center;
  }
  .photo { position: absolute; }
  .photo-model { left: 0; top: 86px; width: 425px; height: 410px;
    background: linear-gradient(135deg, #4a362b 0%, #8c6b56 40%, #d9c4ae 75%, #efe6da 100%); }
  .photo-interior { left: 425px; top: 86px; width: 424px; height: 184px;
    background: linear-gradient(135deg, #cfc6b4, #f1ece2 55%, #a99678); }
  .photo-hair { left: 425px; top: 270px; width: 424px; height: 226px;
    background: linear-gradient(160deg, #24160f, #7a5442 45%, #b88f74 60%, #3a2519); }
  .tagline {
    position: absolute; left: 38px; top: 414px; color: var(--white);
    text-shadow: 0 0 8px rgba(10,10,30,.95), 0 0 3px rgba(0,0,0,.9);
    font-weight: 800; font-size: 31px; line-height: 44px; letter-spacing: 1px;
  }
  .staff-band {
    position: absolute; left: 0; top: 496px; width: 849px; height: 185px; background: var(--white);
  }
  .staff-row {
    position: absolute; left: 28px; top: 518px; width: 793px;
    display: flex; justify-content: space-between;
  }
  .staff-photo { width: 128px; height: 128px;
    background: linear-gradient(160deg, #d2bda9, #8c7160); }
  .staff-photo:nth-child(2n) { background: linear-gradient(160deg, #c0a591, #5e4638); }
  .menu-area {
    position: absolute; left: 0; top: 681px; width: 849px; height: 352px;
    background: var(--cream);
  }
  .pattern-corner {
    position: absolute; left: 560px; top: 1040px; width: 0; height: 0;
  }
  .ornament-corner {
    position: absolute; right: 0; top: 880px; width: 230px; height: 153px;
    background: radial-gradient(ellipse at 100% 100%, rgba(198,161,90,.45), rgba(198,161,90,0) 70%);
  }
  .menu-banner {
    position: absolute; left: 312px; top: 710px; width: 225px; height: 34px;
    background: linear-gradient(90deg, var(--gold-dark), var(--gold-light) 50%, var(--gold-dark));
    color: var(--white); font-family: "Cormorant Garamond", serif; font-weight: 600;
    font-size: 24px; letter-spacing: 8px; display: flex; align-items: center; justify-content: center;
  }
  .menu-list { position: absolute; left: 30px; top: 758px; width: 462px; list-style: none; }
  .menu-item {
    display: flex; justify-content: space-between; font-size: 18px; font-weight: 600;
    line-height: 31px; letter-spacing: .5px;
  }
  .feature-box { position: absolute; left: 540px; width: 270px; }
  .feature-box.face { top: 778px; height: 120px; border-bottom: 1px solid var(--gold); padding-bottom: 10px; }
  .feature-box.consult { top: 948px; height: 80px; }
  .feature-title { font-size: 21px; font-weight: 700; color: var(--navy); line-height: 34px; }
  .feature-line { display: flex; justify-content: space-between; font-size: 15px; line-height: 30px; }
  .feature-note { font-size: 15px; line-height: 30px; }
  .face .feature-title { display: flex; justify-content: space-between; align-items: baseline; }
  .face .feature-title span { font-size: 16px; font-weight: 600; color: var(--ink); }
  .consult .feature-title { border-bottom: 1px solid var(--gold); }
  .footer {
    position: absolute; left: 0; top: 1033px; width: 849px; height: 167px;
    background: var(--navy-deep); color: var(--white);
  }
  .brand-mark {
    position: absolute; left: 14px; top: 14px; width: 170px; height: 140px;
    background: var(--white); display: flex; flex-direction: column;
    align-items: center; justify-content: center; gap: 8px;
  }
  .brand-mark .dot { width: 14px; height: 14px; border-radius: 50%; background: var(--gold); }
  .brand-mark .name { color: var(--navy); font-size: 22px; font-weight: 600; text-align: center; line-height: 1.15; }
  .salon-name { position: absolute; left: 200px; top: 26px; font-size: 19px; font-weight: 600; }
  .phone {
    position: absolute; left: 200px; top: 50px; display: flex; align-items: center; gap: 10px;
    font-family: "Cormorant Garamond", serif; font-weight: 600; font-size: 50px; line-height: 60px; letter-spacing: 1px;
  }
  .address { position: absolute; left: 200px; top: 116px; font-family: "Noto Sans JP", sans-serif; font-size: 11px; line-height: 15px; color: #d6d9e4; }
  .consult-tag {
    position: absolute; left: 580px; top: 8px; width: 240px; height: 26px;
    background: var(--gold); color: var(--white); font-size: 14px; font-weight: 600;
    display: flex; align-items: center; justify-content: center; letter-spacing: 1px;
  }
</style>
</head>
<body>
<main class="flyer">
  <div class="pattern-top" role="img" aria-label="紺地に花柄の装飾模様"></div>
  <div class="reserve-banner">完全予約制</div>

  <div class="photo photo-model" role="img" aria-label="長い巻き髪の女性モデルの写真"></div>
  <div class="photo photo-interior" role="img" aria-label="上質なサロン店内の写真"></div>
  <div class="photo photo-hair" role="img" aria-label="艶のあるストレートヘアの写真"></div>

  <p class="tagline">大切な髪を傷めない<br>最高の髪をつくる一生のパートナーになります</p>

  <div class="staff-band"></div>
  <div class="staff-row">
    <div class="staff-photo" role="img" aria-label="スタッフ写真"></div>
    <div class="staff-photo" role="img" aria-label="スタッフ写真"></div>
    <div class="staff-photo" role="img" aria-label="スタッフ写真"></div>
    <div class="staff-photo" role="img" aria-label="スタッフ写真"></div>
    <div class="staff-photo" role="img" aria-label="スタッフ写真"></div>
  </div>

  <section class="menu-area"></section>
  <div class="ornament-corner" role="img" aria-label="金色の花の装飾"></div>
  <div class="menu-banner">MENU</div>

  <ul class="menu-list">
    <li class="menu-item"><span>トリートメントスパ付きカラー＋カット</span><span>12,300円</span></li>
    <li class="menu-item"><span>カット＋艶髪トリートメント</span><span>10,800円</span></li>
    <li class="menu-item"><span>ストレート＋カット＋トリートメント</span><span>19,600円</span></li>
    <li class="menu-item"><span>パーマ＋カット＋トリートメントスパ</span><span>17,600円</span></li>
    <li class="menu-item"><span>ストレート＋カラーセット</span><span>28,100円</span></li>
    <li class="menu-item"><span>パーマ＋カラーセット</span><span>26,100円</span></li>
    <li class="menu-item"><span>オーダーメイドストレート＋毛先パーマ</span><span>24,500円</span></li>
    <li class="menu-item"><span>ストレート＋パーマ＋艶カラーコース</span><span>33,000円</span></li>
  </ul>

  <div class="feature-box face">
    <p class="feature-title">小顔効果 <span>12,500円</span></p>
    <p class="feature-line"><span>ダイヤモンドカット</span><span>10,800円</span></p>
    <p class="feature-note">リフトアップフェイスケア</p>
  </div>
  <div class="feature-box consult">
    <p class="feature-title">無料カウンセリング</p>
    <p class="feature-note">髪質チェック・お悩み相談</p>
  </div>

  <footer class="footer">
    <div class="brand-mark"><span class="dot"></span><span class="name">Le Chêne<br>Doré</span></div>
    <p class="salon-name">Le Chêne Doré（ルシェヌドレ）</p>
    <p class="phone">
      <svg width="36" height="36" viewBox="0 0 24 24" aria-hidden="true"><path fill="#ffffff" d="M6.6 10.8a15.1 15.1 0 0 0 6.6 6.6l2.2-2.2a1 1 0 0 1 1-.25 11.4 11.4 0 0 0 3.6.57 1 1 0 0 1 1 1V20a1 1 0 0 1-1 1A17 17 0 0 1 3 4a1 1 0 0 1 1-1h3.5a1 1 0 0 1 1 1 11.4 11.4 0 0 0 .57 3.6 1 1 0 0 1-.25 1z"/></svg>
      092-478-5126
    </p>
    <p class="address">https://salon.kamisearch-example.jp/slnK000571832/<br>福岡県福岡市中央区天神4-7-15 ミヤビビル3階<br>営業時間 10:00〜19:00 定休日 毎週火曜日</p>
    <div class="consult-tag">お気軽にご相談ください</div>
  </footer>
</main>
</body>
</html>
```